Building Company Business Card Design

I am looking to get a business card designed for my Building Company. Please find the logo attached.

Industry/Entity Type

Business

Contact Information for Business Card

Mobile 0472 913 046
Email admin@tarrowconstructworks.com.au
Website www.tarrowconstructworks.com.au

Colors
0255a3

```html
<!DOCTYPE html>
<html lang="en">
<head>
<meta charset="utf-8">
<title>Tarrow Constructworks – Business Card</title>
<link href="https://fonts.googleapis.com/css2?family=Arimo:wght@400;700&display=swap" rel="stylesheet">
<style>
  :root {
    --brand-blue: #0255a3;
    --edge-grey: #6d6d70;
    --paper: #ffffff;
    --paper-shade: #f1f1f2;
    --stage: #636068;
    --white: #ffffff;
  }
  * { box-sizing: border-box; margin: 0; padding: 0; }
  html, body {
    width: 1200px; height: 675px; overflow: hidden;
    background: var(--stage);
    font-family: "Arimo", Arial, sans-serif;
  }
  .stage { position: relative; width: 1200px; height: 675px; }

  .card {
    position: absolute;
    width: 520px; height: 297px;
    top: 189px;
    overflow: hidden;
    box-shadow: 0 6px 18px rgba(0,0,0,.35);
  }
  .card--front { left: 60px; background: linear-gradient(135deg, var(--paper) 0%, var(--paper-shade) 100%); }
  .card--back  { left: 620px; background: var(--brand-blue); }

  .card__swoosh { position: absolute; inset: 0; width: 100%; height: 100%; }

  .wordmark {
    position: absolute;
    display: flex; align-items: center; gap: 9px;
    font-weight: 700; text-transform: uppercase; letter-spacing: 0.5px;
    white-space: nowrap;
  }
  .wordmark__dot { width: 11px; height: 11px; border-radius: 50%; flex: none; }
  .card--front .wordmark { left: 30px; top: 100px; font-size: 19px; color: var(--brand-blue); }
  .card--front .wordmark__dot { background: var(--brand-blue); }
  .card--back .wordmark { left: 0; right: 0; top: 133px; justify-content: center; font-size: 26px; letter-spacing: 1px; color: var(--white); }
  .card--back .wordmark__dot { width: 12px; height: 12px; background: var(--white); }

  .contact {
    position: absolute; right: 26px; top: 136px;
    color: var(--white); font-size: 12px; line-height: 19px;
    list-style: none; text-align: right;
  }
  .contact__item { display: flex; justify-content: flex-end; align-items: center; gap: 7px; }
  .contact__icon { width: 10px; height: 10px; flex: none; }

  .person { position: absolute; left: 34px; top: 230px; color: var(--white); }
  .person__name { font-size: 31px; font-weight: 700; line-height: 32px; }
  .person__role { font-size: 12px; margin-top: 2px; }
</style>
</head>
<body>
<main class="stage">

  <section class="card card--front" aria-label="Business card front">
    <svg class="card__swoosh" viewBox="0 0 520 297" preserveAspectRatio="none" aria-hidden="true">
      <path d="M0,214 Q372,184 506,0 L520,0 L520,297 L0,297 Z" fill="var(--edge-grey)"/>
      <path d="M0,222 Q384,192 520,0 L520,297 L0,297 Z" fill="var(--brand-blue)"/>
    </svg>

    <div class="wordmark">
      <span class="wordmark__dot"></span>
      <span class="wordmark__name">Tarrow Constructworks</span>
    </div>

    <ul class="contact">
      <li class="contact__item">0472 913 046
        <svg class="contact__icon" viewBox="0 0 10 10" aria-hidden="true"><rect x="2.5" y="0.5" width="5" height="9" rx="1" fill="none" stroke="#fff"/><circle cx="5" cy="8" r=".6" fill="#fff"/></svg>
      </li>
      <li class="contact__item">admin@tarrowconstructworks.com.au
        <svg class="contact__icon" viewBox="0 0 10 10" aria-hidden="true"><rect x="0.5" y="2" width="9" height="6" fill="#fff"/><path d="M0.5,2 L5,5.5 L9.5,2" fill="none" stroke="var(--brand-blue)" stroke-width=".8"/></svg>
      </li>
      <li class="contact__item">www.tarrowconstructworks.com.au
        <svg class="contact__icon" viewBox="0 0 10 10" aria-hidden="true"><circle cx="5" cy="5" r="4.3" fill="none" stroke="#fff"/><ellipse cx="5" cy="5" rx="1.8" ry="4.3" fill="none" stroke="#fff" stroke-width=".7"/><line x1=".7" y1="5" x2="9.3" y2="5" stroke="#fff" stroke-width=".7"/></svg>
      </li>
    </ul>

    <div class="person">
      <p class="person__name">Liam Carter</p>
      <p class="person__role">Office Manager</p>
    </div>
  </section>

  <section class="card card--back" aria-label="Business card back">
    <div class="wordmark">
      <span class="wordmark__dot"></span>
      <span class="wordmark__name">Tarrow Constructworks</span>
    </div>
  </section>

</main>
</body>
</html>
```